Business Card Design

Stronger Care Network for the Riverlands is a partnership of twenty different health organisations in the western suburbs of Melbourne, working together to improve the health of the local community. The western suburbs of Melbourne is one of the fastest growing and most culturally diverse populations in Australia and its communities have some of the poorest health outcomes in Australia.
Please see location for copy of the SCNR:
http://qvlr.com.au/fileadmin/filemount/pdf_files/SCNFTR_13_FINAL_JUNE_2012.pdf
Updates

Reason: Hello. I've extended the deadline because in the brief I made a confusing mention about a logo, but I actually meant the 'Stronger Care Network for the Riverlands' jpg that I had already attached. Sorry about the confusion Thanks Rosalind

Hello, Thanks for the designs I have already received. I have extended the deadline because I made a confusing reference to a logo in my brief, but I was talking about the 'Stronger Care Network for the Riverlands' jpg I had already attached. There is no other logo for me to provide.

Thanks, Rosalind

Target Market(s)

Health and state/local government managers and CEOs

Industry/Entity Type

Health

Contact Information for Business Card

Rosalind Tiernan
Executive Officer
Stronger Care Network for the Riverlands
Ph: 0438 295 614
Rosalind.Tiernan@kp.org.au

Requirements
Must have
• logo and details as provided.
Would prefer matt finish
I can't see that logo has successfully attached so if it has not, please email or call me to follow up.

```html
<!DOCTYPE html>
<html lang="en">
<head>
<meta charset="utf-8">
<title>Stronger Care Network for the Riverlands — Business Card</title>
<link rel="stylesheet" href="https://fonts.googleapis.com/css2?family=Mulish:wght@400;500;700&family=Zilla+Slab:wght@600;700&display=swap">
<style>
  :root {
    --brand-blue: #0a8acd;
    --brand-green: #bcd864;
    --ink-dark: #2a2a2a;
    --ink-grey: #555555;
    --paper: #ffffff;
    --canvas: #ffffff;
  }
  html, body {
    margin: 0;
    padding: 0;
    overflow: hidden;
  }
  body {
    width: 1200px;
    height: 1000px;
    background: var(--canvas);
    position: relative;
    font-family: "Mulish", sans-serif;
  }
  .card {
    position: absolute;
    left: 240px;
    width: 654px;
    height: 403px;
    overflow: hidden;
    box-shadow: 0 6px 18px rgba(0, 0, 0, 0.18);
  }
  .card--front { top: 89px; background: var(--paper); }
  .card--back  { top: 520px; background: var(--brand-blue); }

  .band {
    position: absolute;
    height: 42px;
    background: var(--brand-green);
  }
  .card--front .band { left: 0; right: 0; top: 267px; }
  .card--back .band--left  { left: 0; width: 232px; top: 267px; }
  .card--back .band--right { left: 422px; right: 0; top: 267px; }

  .brand-square {
    position: absolute;
    left: 53px;
    top: 211px;
    width: 176px;
    height: 155px;
    background: var(--brand-blue);
    display: flex;
    align-items: center;
  }
  .brand-name {
    margin: 0;
    font-family: "Mulish", sans-serif;
    font-weight: 700;
    color: var(--paper);
  }
  .brand-square .brand-name {
    padding: 0 22px 0 36px;
    font-size: 19px;
    line-height: 25px;
  }
  .brand-block {
    position: absolute;
    left: 232px;
    width: 190px;
    top: 100px;
    height: 209px;
    display: flex;
    align-items: flex-end;
  }
  .brand-block .brand-name {
    padding: 0 14px 0 26px;
    font-size: 27px;
    line-height: 35px;
  }

  .details {
    position: absolute;
    right: 64px;
    top: 56px;
    text-align: right;
  }
  .details p { margin: 0; white-space: nowrap; }
  .person-name {
    font-size: 31px;
    font-weight: 500;
    color: var(--brand-blue);
    line-height: 38px;
  }
  .person-role {
    font-size: 24px;
    color: var(--ink-dark);
    line-height: 32px;
  }
  .org-name {
    font-family: "Zilla Slab", serif;
    font-weight: 700;
    font-size: 18px;
    color: var(--ink-grey);
    line-height: 30px;
  }
  .contact {
    font-size: 17px;
    color: var(--ink-grey);
    line-height: 27px;
  }
</style>
</head>
<body>
  <section class="card card--front" aria-label="Business card front">
    <div class="band"></div>
    <div class="brand-square">
      <p class="brand-name">Stronger Care Network for the Riverlands</p>
    </div>
    <div class="details">
      <p class="person-name">Rosalind Tiernan</p>
      <p class="person-role">Executive Officer</p>
      <p class="org-name">Stronger Care Network for the Riverlands</p>
      <p class="contact">Rosalind.Tiernan@kp.org.au</p>
      <p class="contact">Ph:&nbsp; 0438 295 614</p>
    </div>
  </section>

  <section class="card card--back" aria-label="Business card back">
    <div class="band band--left"></div>
    <div class="band band--right"></div>
    <div class="brand-block">
      <p class="brand-name">Stronger Care Network for the Riverlands</p>
    </div>
  </section>
</body>
</html>
```